Stationary & Business Card for a Rock climbing company based primarily in Joshua Tree NP
Use provided logo
Stationary & Business Card for a Rock climbing company based primarily in Joshua Tree NP - Outdoors
Creative Brief
Simple
Garrick Fenn
Director
27615 Marrow Lane Victorville, CA 92307
garrickfenn@mailbrook.com
www.ridgepathoutfitters.com

```html
<!DOCTYPE html>
<html lang="en">
<head>
<meta charset="utf-8">
<title>Ridgepath Outfitters – Business Card</title>
<link href="https://fonts.googleapis.com/css2?family=Open+Sans:wght@400;600;700&display=swap" rel="stylesheet">
<style>
  :root {
    --stage: #6b6b6b;
    --card: #ffffff;
    --ink: #2b2b2b;
    --muted: #555555;
    --orange: #f0961e;
    --brown: #3a1f12;
  }
  * { box-sizing: border-box; margin: 0; padding: 0; }
  html, body { width: 1200px; height: 908px; overflow: hidden; }
  body {
    background: var(--stage);
    font-family: "Open Sans", Arial, sans-serif;
    display: flex;
    align-items: center;
    justify-content: center;
    gap: 40px;
  }
  .card {
    position: relative;
    width: 540px;
    height: 310px;
    background: var(--card);
    border-radius: 16px;
    overflow: hidden;
    box-shadow: 0 6px 18px rgba(0,0,0,0.25);
  }
  .brand {
    position: absolute;
    display: flex;
    align-items: center;
    gap: 12px;
  }
  .brand-dot {
    width: 54px; height: 54px;
    border-radius: 50%;
    background: var(--orange);
    flex: none;
  }
  .brand-name {
    font-weight: 700;
    color: var(--brown);
    font-size: 22px;
    line-height: 1.1;
    text-transform: uppercase;
    letter-spacing: 1px;
  }
  .card-front .brand {
    left: 50%; top: 50%;
    transform: translate(-50%, -50%);
  }
  .card-back .brand {
    left: 34px; top: 188px;
  }
  .card-back .brand-name { font-size: 18px; }
  .card-back .brand-dot { width: 44px; height: 44px; }
  .swoosh { position: absolute; inset: 0; }
  .contact {
    position: absolute;
    left: 270px; top: 34px;
    color: var(--muted);
    font-size: 11px;
    line-height: 1.55;
  }
  .contact-name { font-size: 22px; font-weight: 600; color: var(--ink); line-height: 1.2; }
  .contact-role { font-size: 15px; font-weight: 600; color: var(--orange); margin-bottom: 8px; }
  .contact-line { display: flex; align-items: center; gap: 6px; }
  .contact-icon { width: 11px; height: 11px; flex: none; }
</style>
</head>
<body>
  <section class="card card-front">
    <div class="brand">
      <span class="brand-dot"></span>
      <span class="brand-name">Ridgepath<br>Outfitters</span>
    </div>
  </section>

  <section class="card card-back">
    <svg class="swoosh" viewBox="0 0 540 310" aria-hidden="true">
      <path d="M540 10 C500 190 370 285 40 310 L120 310 C400 292 520 200 540 48 Z" fill="var(--orange)"/>
      <path d="M540 48 C520 200 400 292 120 310 L540 310 Z" fill="var(--brown)"/>
    </svg>
    <div class="contact">
      <div class="contact-name">Garrick Fenn</div>
      <div class="contact-role">Director</div>
      <div>27615 Marrow Lane</div>
      <div>Victorville, CA 92307</div>
      <div class="contact-line">
        <svg class="contact-icon" viewBox="0 0 12 12"><circle cx="6" cy="6" r="6" fill="var(--orange)"/><path d="M4 3 L5 3 L5.6 4.6 L4.9 5.2 Q5.6 6.6 6.8 7.1 L7.4 6.4 L9 7 L9 8 Q6 9 3.5 4.5 Z" fill="#fff"/></svg>
        (760) 555-0148
      </div>
      <div class="contact-line">
        <svg class="contact-icon" viewBox="0 0 12 12"><circle cx="6" cy="6" r="6" fill="var(--orange)"/><path d="M4 3 L5 3 L5.6 4.6 L4.9 5.2 Q5.6 6.6 6.8 7.1 L7.4 6.4 L9 7 L9 8 Q6 9 3.5 4.5 Z" fill="#fff"/></svg>
        (760) 555-0172
      </div>
      <div class="contact-line">
        <svg class="contact-icon" viewBox="0 0 12 12"><circle cx="6" cy="6" r="6" fill="var(--orange)"/><rect x="3" y="4" width="6" height="4.2" fill="none" stroke="#fff" stroke-width="0.9"/><path d="M3 4 L6 6.4 L9 4" fill="none" stroke="#fff" stroke-width="0.9"/></svg>
        garrickfenn@mailbrook.com
      </div>
      <div class="contact-line">
        <svg class="contact-icon" viewBox="0 0 12 12"><circle cx="6" cy="6" r="6" fill="var(--orange)"/><circle cx="6" cy="6" r="3" fill="none" stroke="#fff" stroke-width="0.9"/><path d="M3 6 H9 M6 3 V9" stroke="#fff" stroke-width="0.8"/></svg>
        www.ridgepathoutfitters.com
      </div>
    </div>
    <div class="brand">
      <span class="brand-dot"></span>
      <span class="brand-name">Ridgepath<br>Outfitters</span>
    </div>
  </section>
</body>
</html>
```